New Menu Design for edgy barbershop (with bar)

We have a basic graphic for a brand new membership menu. The menu will be located on the wall in our lobby area -- we are planning on making this a very large graphic, but I don't have exact dimensions.

We are a barbershop with a bar & the hottest lady barbers around. We strive to keep a western / saloon feel throughout the barbershop. We cater to mostly a male clientele, so want to have a masculine feel to any creative additions.

I have attached the graphic we started with -- we want to keep the general set up and flow, but are open to your creative brilliance! Our logo is also attached & you can get a good feel for our style on our website: www.ridgelinetrim.example or on our Facebook page: www.facebook.com/ridgelinetrim.

Let me know if you have any questions, or if you need more detail on any of these elements!

A few key details:
- All designs should be horizontal
- The main focus is on the memberships. We want these to pop, and wow customers -- attention should focus on memberships in the graphic, draw the eye in and look glorious.
- We won't look at designs that are too busy or cluttered. Needs to be easy to read & not overwhelming (even with all the information)
- Not too keen on background imagery or color splashes as these make it too complicated. The visual interest should be in how awesome the memberships are!
- Needs to have a clean, masculine feel. Less is more with the background graphics & focus is on getting the info out and drawing people into the awesome memberships we sell.

Target Market(s)

Men 21-65

Font styles to use
Sans Serif

Requirements
Must have
• Masculine feel, western / Saloon theme. Must have all the info included in the graphic slide.
• - Must be Horizontal
• - Must focus on the memberships (need to make the "wow" and drive people to buy them.
Nice to have
• Additional creative elements that really showcase the memberships as awesome!
Should not have
• - No vertical layouts
• - Overly added graphics or background imagery

```html
<!DOCTYPE html>
<html lang="en">
<head>
<meta charset="utf-8">
<title>Ridgeline Trim — Services &amp; Memberships</title>
<link rel="stylesheet" href="https://fonts.googleapis.com/css2?family=Smokum&family=Rye&family=Oswald:wght@300;400;500&family=Alfa+Slab+One&family=Roboto:wght@300;400&display=swap">
<style>
:root{
  --bg-dark:#17110c;
  --bg-mid:#2b2018;
  --orange:#f39a1f;
  --white:#f4efe8;
  --muted:#d8d0c6;
  --red:#e0242a;
  --panel:#120d09;
}
*{margin:0;padding:0;box-sizing:border-box}
html,body{width:1200px;height:880px;overflow:hidden;background:#e9e9e9}
.menu{
  position:relative;width:1200px;height:880px;overflow:hidden;
  background:radial-gradient(ellipse at 45% 45%,#3a2c20 0%,var(--bg-mid) 40%,var(--bg-dark) 100%);
  color:var(--white);font-family:"Oswald",sans-serif;
}
.abs{position:absolute}
/* brand */
.brand{left:0;top:82px;width:700px;text-align:center;white-space:nowrap;
  font-family:"Oswald",sans-serif;font-weight:500;font-size:44px;line-height:1;color:var(--orange)}
.tagline{left:0;width:700px;top:170px;text-align:center;font-family:"Smokum",serif;font-size:29px;color:var(--white);white-space:nowrap}
.tagline span{color:var(--orange);margin:0 8px}
.section-title{left:0;width:700px;top:222px;text-align:center;font-family:"Smokum",serif;font-weight:400;font-size:30px;letter-spacing:6px;color:var(--orange)}
.section-rule{left:300px;top:265px;width:100px;border-top:1px dashed var(--orange)}
/* services */
.service{position:absolute;width:300px}
.service h3{font-family:"Smokum",serif;font-weight:400;font-size:20px;line-height:1;color:var(--orange);letter-spacing:.5px;text-transform:uppercase}
.service .price{position:absolute;right:0;top:0;font-family:"Smokum",serif;font-size:18px;line-height:1;color:var(--white)}
.service p{font-size:11.5px;font-weight:300;line-height:1.4;color:var(--muted);margin-top:6px;width:260px}
.col-left .service{left:31px}
.col-mid .service{left:366px;width:292px}
.col-mid .service p{width:262px}
.divider{left:694px;top:123px;height:675px;border-left:1px dashed var(--orange)}
.location{left:28px;top:810px;font-family:"Roboto",sans-serif;font-size:14px;line-height:1.4}
.location .label{color:var(--orange)}
.follow{left:327px;top:846px;font-family:"Roboto",sans-serif;font-size:15px;color:var(--orange);display:flex;align-items:center;gap:6px}
.follow i{display:inline-block;width:16px;height:16px;border-radius:50%;background:var(--white)}
.photo{left:480px;top:606px;width:160px;height:274px;border-radius:70px 70px 0 0;
  background:linear-gradient(180deg,#c9a27a 0%,#8b6a4e 45%,#1d1915 100%)}
/* membership panel */
.panel{left:733px;top:199px;width:436px;height:650px;border:2px dashed var(--orange);border-radius:22px;background:rgba(10,7,5,.35)}
.pole{left:906px;top:28px;width:92px;height:86px;border-radius:10px;
  background:radial-gradient(circle at 50% 40%,#ff6b6b 0%,#b0202a 40%,rgba(40,30,30,0) 72%)}
.badge{left:810px;top:110px;width:284px;height:180px}
.badge-text{left:810px;top:130px;width:284px;text-align:center;font-family:"Alfa Slab One",serif;font-weight:400;line-height:1}
.badge-text .big{font-size:44px;color:var(--orange)}
.badge-text .small{font-size:26px;color:var(--white);margin-top:6px;line-height:1.1}
.lights{left:905px;top:292px;width:95px;display:flex;justify-content:space-between}
.lights i{width:18px;height:10px;border-radius:50%;background:var(--red);box-shadow:0 0 14px 6px rgba(224,36,42,.7)}
.group-title{left:733px;width:436px;text-align:center;font-family:"Smokum",serif;font-weight:400;font-size:19px;color:var(--white)}
.group-title.orange{color:var(--orange)}
.options{left:733px;width:436px;display:flex;justify-content:space-around}
.option{display:flex;flex-direction:column;align-items:center;width:100px}
.option .icon{width:76px;height:44px;border-radius:12px 12px 6px 6px;background:linear-gradient(180deg,#f6b445,#b96414)}
.option .name{font-family:"Rye",serif;font-size:13px;color:var(--white);margin-top:4px;text-align:center;line-height:1}
.option svg{margin-top:2px}
.visit{position:absolute;top:506px;width:36px;height:36px;border-radius:50%;border:2px solid var(--orange);
  box-shadow:0 0 10px rgba(243,154,31,.8);background:var(--panel);
  font-family:"Alfa Slab One",serif;font-size:19px;line-height:32px;text-align:center;color:var(--white)}
.perks{left:760px;top:712px;width:400px;font-family:"Roboto",sans-serif;font-size:14px;font-weight:300;line-height:1.55}
.perks .head{color:var(--orange);font-weight:400}
.perks ul{list-style:none;padding-left:8px}
.perks li::before{content:"•";color:var(--orange);margin-right:7px}
.site{left:733px;top:839px;width:436px;display:flex;align-items:center;gap:8px}
.site hr{flex:1;border:0;border-top:1px dashed var(--orange)}
.site span{font-family:"Oswald",sans-serif;font-size:13px;letter-spacing:3px;color:var(--orange);background:var(--bg-dark);padding:0 4px}
</style>
</head>
<body>
<main class="menu">

  <header>
    <div class="abs brand">Ridgeline Trim</div>
    <div class="abs tagline">HOT BARBERS<span>★</span>COLD BEER<span>★</span>GREAT HAIRCUTS</div>
    <h2 class="abs section-title">HAIRCUT SERVICES</h2>
    <div class="abs section-rule"></div>
  </header>

  <section class="col-left">
    <article class="service" style="top:302px"><h3>The Cowboy Cut</h3><span class="price">$25</span>
      <p>Our full service cut. Hair Cut, Hot Towel, Double Trough Wash, and Straight Razor Neck Shave</p></article>
    <article class="service" style="top:372px"><h3>The Cowgirl Cut</h3><span class="price">$25</span>
      <p>Our Ladies Cut. Hair Cut, Trough Wash</p></article>
    <article class="service" style="top:426px"><h3>The Terry</h3><span class="price">$17</span>
      <p>Haircut, Double Trough Wash, Hot Towel, and Straight Razor Neck Shave. This is for cowboys that haven't been blessed with a full head of hair. We know it's not fair, that's why your price is!</p></article>
    <article class="service" style="top:528px"><h3>Buzzed Cowboy</h3><span class="price">$22</span>
      <p>Buzz Cut &amp; two beers, for the straightforward cowboy. Must be 21+ for this bad boy.</p></article>
    <article class="service" style="top:597px"><h3>The Little Cowboy and Cowgirl</h3><span class="price">$15</span>
      <p>Kids Cuts 14 and under Hair Cut, Trough Wash, and Neck Trim</p></article>
    <article class="service" style="top:668px"><h3>The Cowboy Package</h3><span class="price">$35</span>
      <p>Cowboy and Little Cowboy Hair Cut</p></article>
    <article class="service" style="top:722px"><h3>Cowboy Razor Fade</h3><span class="price">$30</span>
      <p>Razor Fade, Hot Towel, Double Wash</p></article>
  </section>

  <section class="col-mid">
    <article class="service" style="top:302px"><h3>The Double Scrape</h3><span class="price">$30</span>
      <p>We will take a not so rusty straight razor and get rid of your winter scruff. A face shave with and against the grain</p></article>
    <article class="service" style="top:372px"><h3>The Scalp Scrape</h3><span class="price">$30</span>
      <p>We will take a not so rusty straight razor and get rid of your carrot top.</p></article>
    <article class="service" style="top:436px"><h3>The Colorado</h3><span class="price">$10</span>
      <p>Electric trim your man bush(beard) just how you like it!</p></article>
    <article class="service" style="top:489px"><h3>Rough Rider</h3><span class="price">$10</span>
      <p>Straight razor back of the neck shave &amp; two beers to keep your trail rides smooth.</p></article>
    <article class="service" style="top:555px"><h3>Eyebrow Wax</h3><span class="price">$10</span>
      <p>We can wax them both off, one off, or just touch them up. Add on to any cut.</p></article>
  </section>

  <div class="abs photo" role="img" aria-label="Photo of a barber seated in a barber chair holding a beer"></div>

  <div class="abs location"><span class="label">Located at</span><br>1875 Canyon Rd Elkhorn, CO<br><span class="label">or</span> find our Mobile Barber Shop Near You!</div>
  <div class="abs follow">Follow Us : <i></i><i></i></div>

  <div class="abs divider"></div>

  <section class="membership">
    <div class="abs panel"></div>
    <div class="abs pole" role="img" aria-label="Glowing barber pole with crossed scissors and combs"></div>
    <svg class="abs badge" viewBox="0 0 284 180" aria-hidden="true">
      <polygon points="30,8 254,8 276,50 276,130 254,172 30,172 8,130 8,50" fill="#0d0907" stroke="#f39a1f" stroke-width="3"/>
      <line x1="96" y1="160" x2="132" y2="160" stroke="#f39a1f" stroke-dasharray="3 3"/>
      <line x1="152" y1="160" x2="188" y2="160" stroke="#f39a1f" stroke-dasharray="3 3"/>
    </svg>
    <h2 class="abs badge-text"><div class="big">CHOOSE</div><div class="small">YOUR OWN<br>MEMBERSHIP</div></h2>
    <div class="abs lights"><i></i><i></i><i></i></div>

    <h3 class="abs group-title" style="top:316px">CHOOSE YOUR SERVICE</h3>
    <div class="abs options" style="top:354px">
      <div class="option"><div class="icon" role="img" aria-label="Beer mugs illustration"></div><div class="name">Cowboy</div>
        <svg width="70" height="14"><path d="M2 2 Q35 22 68 2" fill="none" stroke="#f39a1f" stroke-width="2.5"/></svg></div>
      <div class="option"><div class="icon" role="img" aria-label="Beer mugs illustration"></div><div class="name">Little Cowboy</div>
        <svg width="70" height="14"><path d="M2 2 Q35 22 68 2" fill="none" stroke="#f39a1f" stroke-width="2.5"/></svg></div>
      <div class="option"><div class="icon" role="img" aria-label="Beer mugs illustration"></div><div class="name">Shave</div>
        <svg width="70" height="14"><path d="M2 2 Q35 22 68 2" fill="none" stroke="#f39a1f" stroke-width="2.5"/></svg></div>
    </div>

    <h3 class="abs group-title orange" style="top:466px">CHOOSE YOUR VISITS (IN WEEKS)</h3>
    <div class="abs visit" style="left:761px">1</div>
    <div class="abs visit" style="left:822px">2</div>
    <div class="abs visit" style="left:896px">3</div>
    <div class="abs visit" style="left:967px">4</div>
    <div class="abs visit" style="left:1030px">5</div>
    <div class="abs visit" style="left:1103px">6</div>

    <h3 class="abs group-title" style="top:564px">CHOOSE YOUR EXTRAS</h3>
    <div class="abs options" style="top:598px">
      <div class="option"><div class="icon" role="img" aria-label="Beer mugs illustration"></div><div class="name">Free Beer</div>
        <svg width="70" height="14"><path d="M2 2 Q35 22 68 2" fill="none" stroke="#f39a1f" stroke-width="2.5"/></svg></div>
      <div class="option"><div class="icon" role="img" aria-label="Beer mugs illustration"></div><div class="name">Eyebrow Wax</div>
        <svg width="70" height="14"><path d="M2 2 Q35 22 68 2" fill="none" stroke="#f39a1f" stroke-width="2.5"/></svg></div>
      <div class="option"><div class="icon" role="img" aria-label="Beer mugs illustration"></div><div class="name">Colorado</div>
        <svg width="70" height="14"><path d="M2 2 Q35 22 68 2" fill="none" stroke="#f39a1f" stroke-width="2.5"/></svg></div>
      <div class="option"><div class="icon" role="img" aria-label="Beer mugs illustration"></div><div class="name">Unlimited Neck Shaves</div>
        <svg width="70" height="14"><path d="M2 2 Q35 22 68 2" fill="none" stroke="#f39a1f" stroke-width="2.5"/></svg></div>
    </div>

    <div class="abs perks">
      <p><span class="head">THE PERKS</span> (included with all memberships)</p>
      <ul>
        <li>Discounts on additional services, products &amp; drinks!</li>
        <li>Reduced rate for private parties &amp; after-hours events!</li>
        <li>Deals for friends &amp; referral bonuses for you!</li>
        <li>Additional specials, invitations &amp; access throughout the year!</li>
      </ul>
    </div>
    <div class="abs site"><hr><span>WWW.RIDGELINETRIM.EXAMPLE</span><hr></div>
  </section>

</main>
</body>
</html>
```